Website - Ease Spine Ache (wordpress)

We are looking for a complete re-design of our website (worldspinehelp.example) and email template.

The site is not currently Wordpress, but we want a Wordpress Theme and we will move the existing content across.

Our new site needs to look professional and credible, and move away from the 'sales pitch' theme that is currently in use.

Your submissions for the contest should consist of the following design files:
1. New home page for WorldSpineHelp.example

We have a new logo (attached), that I'd like on your site.
Updates

I'd love to see all the following separate sections on the page:
1. an inspirational message  - like the section "united we are 10,000 flight specialists" section on this site: http://sitegallery.example/showcase/northern-coastal-airways/    (but a smaller section)
2. 'what people are saying" (grab some quotes from the testimonials section on Worldspinehelp.example)
3. a promo for buying the 'EaseSpineAche' book 
4. link to the latest blogs - maximum 10 links, with 'more..' (see current home page)
5. link to the latest articles (see current homepage)
6. the 'sales pitch' for buying all the books
7. the 'sales pitch' for downloading the free ebook
8. photo, "Peter Dawson"
9. some stock photos (I will purchase these if you can find some examples) to pretty up the page

A site we like is  http://drquellen.example/  (but a bit simpler - less busy).

Preference is for a site with muted blues/blue grey/white.

Plenty of good stock  photo ideas here:

I'm happy to purchase them if you can come up with the ideas/layout etc...

Reason: I've changed the brief, so I'd like to extend the deadline. The current designs are looking good, but I've added the new logo to the brief to be incorporated, and in a couple days will have new covers for the ebooks. Thanks, Nora

I've attached a vector file (and cdr file) for the new logo.

Can you please use this on the site?

Target Market(s)

People looking online for help fixing their back pain. The site needs to convert clicks to sales.

Industry/Entity Type

Sales

Requirements
Must have
• REQUIRED FOR CONTEST:

HOMEPAGE
- Homepage with dark blue background
- lighter blue banner with the logo and photo
- Photo of Peter Dawson
- 'what people are saying" (I've attached some text in file)
-a promo for buying the 'EaseSpineAche' book
- link to the blogs
- link to the latest articles (see current homepage)
- the 'sales pitch' for buying all the books
- the 'sales pitch' for downloading the free ebook
- photo, "Peter Dawson"
- some stock photos

NOT REQUIRED FOR CONTEST:
These items aren't required for the contest, but we expect the winner to provide the following items:

SALES PAGE
There is an additional webpage needing re-design: to-spinerelief.example.
This site is getting lots of traffic, but not converting to many sales. It's a single page, but needs a complete overhaul. The sole purpose of this page is to get people to purchase the books.

ADDITIONAL CONTENT PAGES
- additional designs for the other pages on WorldSpineHelp.example, e.g. Blog, About Us, Contact Us etc... (Wordpress)

EMAIL TEMPLATE
We require an email template to be used for the auto-responder. Two different designs will be required (winner will be given further instructions - very easy).

Nice to have
• stock photos - see the update.
Should not have
• - any logo or text from existing site (it's dreadful!) I want something completely new.

Fonts, layout etc...

```html
<!DOCTYPE html>
<html lang="en">
<head>
<meta charset="utf-8">
<title>Ease Spine Ache</title>
<link href="https://fonts.googleapis.com/css2?family=Arimo:wght@400;700&display=swap" rel="stylesheet">
<style>
:root{
  --header-bg:#eeeceb;
  --blue:#1f6db3;
  --blue-dark:#0d5aa3;
  --blue-light:#2e8fd0;
  --navy:#1d2a6b;
  --red:#b0121a;
  --text:#333;
  --panel-edge:#b9b9b9;
  --btn-top:#5bb7ee;
  --btn-bot:#1f86cc;
}
*{box-sizing:border-box;margin:0;padding:0}
html,body{width:1049px;height:1200px;overflow:hidden}
body{font-family:Arimo,Arial,sans-serif;background:#fff;color:var(--text);position:relative}
.abs{position:absolute}
.site-header{left:0;top:0;width:1049px;height:127px;background:var(--header-bg)}
.logo{left:175px;top:52px;display:flex;align-items:center;gap:8px;color:var(--blue);font-size:27px;font-weight:400}
.logo-dot{width:12px;height:12px;border-radius:50%;background:var(--blue)}
.call{left:730px;top:17px;display:flex;align-items:center;gap:6px;font-size:11px;font-weight:700;color:#333}
.call-icon{width:24px;height:22px;background:#4a6f95;border-radius:4px;display:flex;align-items:center;justify-content:center}
.social{left:790px;top:102px;display:flex;gap:6px}
.social span{width:26px;height:26px;border-radius:3px;background:#3f7fc0;color:#fff;font-size:6px;font-weight:700;display:flex;align-items:center;justify-content:center}
.main-nav{left:0;top:127px;width:1049px;height:42px;background:#fff;border-bottom:3px solid var(--blue-dark)}
.main-nav ul{list-style:none;display:flex;position:absolute;left:176px;top:0;height:39px}
.main-nav li{font-size:10.5px;color:#333;padding:0 16px;line-height:39px}
.main-nav li.current{background:var(--blue);color:#fff;padding:0 13px}
.hero-band{left:0;top:169px;width:1049px;height:284px;background:linear-gradient(180deg,var(--blue-light),var(--blue-dark))}
.slider{left:164px;top:179px;width:720px;height:263px;background:#fff;border-radius:3px;box-shadow:0 8px 10px -6px rgba(0,0,0,.35)}
.slide-photo{left:4px;top:4px;width:389px;height:255px;background:linear-gradient(180deg,#9cc9ef 0%,#8fbbe0 40%,#3f6ea6 60%,#4a6a4a 75%,#1e2a3e 100%)}
.slide-copy{left:413px;top:34px;width:302px;text-align:center}
.slide-copy h1{font-size:17px;color:var(--red);font-weight:700}
.slide-copy p{margin-top:66px;font-size:14px;font-weight:700;color:var(--navy);line-height:17px}
.btn{display:block;width:82px;height:22px;border-radius:3px;background:linear-gradient(180deg,var(--btn-top),var(--btn-bot));color:#fff;font-size:11px;font-weight:700;text-align:center;line-height:22px;box-shadow:0 1px 2px rgba(0,0,0,.3)}
.slide-btn{left:590px;top:181px}
.dots{left:631px;top:248px;display:flex;gap:4px}
.dots i{width:11px;height:11px;border-radius:50%;background:#111}
.dots i.on{background:var(--blue)}
.panel{left:167px;width:714px;height:173px;border:2px solid var(--panel-edge);background:linear-gradient(180deg,#fff 55%,#e6e6e6);box-shadow:0 3px 4px rgba(0,0,0,.2)}
.welcome{top:474px}
.welcome-photo{left:10px;top:15px;width:185px;height:124px;border:3px solid #fff;box-shadow:0 0 3px #999;background:linear-gradient(135deg,#e05a3a,#3aa0d8 45%,#f4c23a 75%,#7cbf4a)}
.panel h2{font-size:18px;color:var(--red);font-weight:700}
.welcome h2{left:243px;top:18px}
.welcome p{left:212px;top:54px;width:496px;font-size:8.9px;font-weight:700;line-height:16px;color:#333}
.welcome .btn{left:606px;top:131px}
.articles{top:662px}
.articles h2{left:0;top:9px;width:710px;text-align:center}
.thumb{top:36px;border:1px solid #ccc;background:linear-gradient(180deg,#d8d8d8,#8a8a8a)}
.cap{top:134px;font-size:14px;font-weight:700;color:var(--navy)}
.articles .b1{left:615px;top:56px}
.articles .b2{left:615px;top:90px}
.card{top:861px;width:227px;height:166px;border:1px solid #cfcfcf;border-radius:4px;background:linear-gradient(180deg,#fff,#e9e9e9);box-shadow:0 2px 3px rgba(0,0,0,.15)}
.card h3{position:absolute;top:4px;width:100%;text-align:center;font-size:17px;color:var(--red);font-weight:700}
.card p{position:absolute;font-size:8.5px;font-weight:700;line-height:15.5px;color:#333}
.card p.tight{font-size:8px}
.more{position:absolute;font-size:8.5px;font-style:italic;font-weight:700;color:var(--red)}
.icon{position:absolute;border-radius:10px}
.site-footer{left:0;top:1076px;width:1049px;height:124px;background:linear-gradient(180deg,var(--blue-light),var(--blue-dark))}
.paywell{left:167px;top:13px;width:71px;height:45px;background:#fff;border:2px solid #f2c27a;color:var(--navy);font-size:14px;font-weight:700;display:flex;align-items:center;justify-content:center}
.cards{left:249px;top:15px;display:flex;gap:4px}
.cards span{width:36px;height:24px;background:#fff;color:var(--navy);font-size:8px;font-weight:700;display:flex;align-items:center;justify-content:center}
.buy{left:263px;top:46px;width:127px;height:30px;border-radius:15px;background:linear-gradient(180deg,#ffe29a,#f5a623);border:1px solid #d08a1a;color:var(--navy);font-size:15px;font-weight:700;font-style:italic;text-align:center;line-height:28px}
.foot-nav{right:176px;top:72px;display:flex;gap:7px;font-size:8.5px;color:#fff}
.copyright{right:176px;top:99px;font-size:8px;color:#a9d3f2;font-weight:700}
</style>
</head>
<body>
<header class="site-header abs">
  <div class="logo abs"><span class="logo-dot"></span>Ease Spine Ache</div>
  <div class="call abs"><span class="call-icon"><svg width="14" height="12" viewBox="0 0 14 12"><path d="M1 4c3-3 9-3 12 0l-2 2-2-1V3H5v2L3 6z" fill="#fff"/><rect x="3" y="7" width="8" height="4" rx="1" fill="#fff"/></svg></span>Call us&nbsp;&nbsp; (555) 0142 7788</div>
  <div class="social abs"><span>Chirpa</span><span>ProNet</span><span>Friendo</span></div>
</header>
<nav class="main-nav abs">
  <ul>
    <li class="current">Home</li><li>About us</li><li>Articles</li><li>Products</li><li>Testimonials</li><li>Diagonistic Service</li><li>Blog</li><li>Free E books</li><li>Contact Us</li>
  </ul>
</nav>
<section class="hero-band abs"></section>
<section class="slider abs">
  <div class="slide-photo abs" role="img" aria-label="Photo of a smiling couple jogging outdoors by the sea"></div>
  <div class="slide-copy abs">
    <h1>Do You Suffer From BACK PAIN?</h1>
    <p>Would you like to know to take control of your pain and fix it yourself?</p>
  </div>
  <a class="btn slide-btn abs">Read More</a>
  <div class="dots abs"><i></i><i></i><i class="on"></i><i></i><i></i></div>
</section>
<section class="panel welcome abs">
  <div class="welcome-photo abs" role="img" aria-label="Photo of a large happy group of people of all ages"></div>
  <h2 class="abs">Welcome to our Website...</h2>
  <p class="abs">"Lorem ipsum dolor sit amet, consectetur adipisicing elit, sed do eiusmod tempor incididunt ut labore et dolore magna aliqua. Ut enim ad minim veniam, quis nostrud exercitation ullamco laboris nisi ut aliquip ex ea commodo consequat. Duis aute irure dolor in reprehenderit in voluptate velit esse cillum dolore eu fugiat nulla pariatur. Excepteur sint occaecat cupidatat non proident, sunt in culpa qui officia deserunt mollit anim id est laborum."</p>
  <a class="btn abs">Read More</a>
</section>
<section class="panel articles abs">
  <h2 class="abs">Our Articles...</h2>
  <div class="thumb abs" style="left:21px;width:149px;height:88px;background:linear-gradient(180deg,#cfcfcf,#4a4a4a)" role="img" aria-label="Photo of a man stretching at his office desk"></div>
  <div class="thumb abs" style="left:196px;width:129px;height:88px;background:linear-gradient(180deg,#f1f1f1,#b5b5b5)" role="img" aria-label="Photo of a woman stretching her arms at a bright desk"></div>
  <div class="thumb abs" style="left:357px;width:129px;height:88px;background:linear-gradient(180deg,#f4f4f4,#9a9a9a)" role="img" aria-label="Photo of a businessman holding his aching back"></div>
  <div class="thumb abs" style="left:507px;top:34px;width:85px;height:95px;background:linear-gradient(180deg,#b97a4a,#e8e2d8)" role="img" aria-label="Photo of a man hunched in a cramped box office"></div>
  <span class="cap abs" style="left:22px">BACK PAIN AT WORK</span>
  <span class="cap abs" style="left:195px">BACK PAIN RELIEF</span>
  <span class="cap abs" style="left:360px">MY BACK PAIN</span>
  <span class="cap abs" style="left:485px">SIT UP STRAIGHT</span>
  <a class="btn b1 abs">Order Now</a>
  <a class="btn b2 abs">Read More</a>
</section>
<section class="card abs" style="left:172px">
  <h3>Testimonials</h3>
  <div class="icon" style="left:6px;top:40px;width:64px;height:64px;background:linear-gradient(180deg,#4cb8ee,#1a79c0)" role="img" aria-label="Testimonials speech bubble icon"></div>
  <p style="left:78px;top:32px;width:140px">Lorem ipsum dolor sit amet, consectetur adipisicing elit, sed do eiusmod tempor incididunt ut labore et dolore magna aliqua. Ut enim ad minim veniam, quis nostrud ullamco laboris nisi ut .</p>
  <span class="more" style="left:154px;top:152px">Read more...</span>
</section>
<section class="card abs" style="left:409px">
  <h3>Free E-Books</h3>
  <div class="icon" style="left:8px;top:45px;width:62px;height:70px;border-radius:3px;background:linear-gradient(180deg,#f4f4f4,#d6d6d6);border:1px solid #bbb" role="img" aria-label="Document download icon"></div>
  <p style="left:84px;top:36px;width:140px">Lorem ipsum dolor sit amet, consectetur adipisicing elit, sed do eiusmod tempor incididunt ut labore et dolore magna aliqua. Ut enim ad minim veniam, quis nostrud ullamco laboris nisi ut .</p>
  <span class="more" style="left:159px;top:152px">Read more...</span>
</section>
<section class="card abs" style="left:647px">
  <h3>Blog</h3>
  <div class="icon" style="left:2px;top:50px;width:58px;height:58px;background:linear-gradient(180deg,#f89a4a,#e05a14)" role="img" aria-label="Blog feed icon"></div>
  <p class="tight" style="left:63px;top:36px;width:164px">Lorem ipsum dolor sit amet, consectetur adipisicing elit, sed do eiusmod tempor incididunt.</p>
  <span class="more" style="left:162px;top:79px">Read more...</span>
  <p class="tight" style="left:63px;top:99px;width:164px">Lorem ipsum dolor sit amet, consectetur adipisicing elit, sed do eiusmod tempor incididunt.</p>
  <span class="more" style="left:162px;top:145px">Read more...</span>
</section>
<footer class="site-footer abs">
  <div class="paywell abs">PayWell</div>
  <div class="cards abs"><span>Orbit</span><span>Vanta</span><span>Azure</span><span>Juno</span><span>BANK</span></div>
  <div class="buy abs">Buy Now</div>
  <div class="foot-nav abs"><span>Home</span><span>About us</span><span>Articles</span><span>Products</span><span>Testimonials</span><span>Diagonistic Service</span><span>Blog</span><span>Free E books</span><span>Contact Us</span></div>
  <div class="copyright abs">Copyright 2012. All Rights Reserved World Spine Help.</div>
</footer>
</body>
</html>
```